Soy Candle Business needs a label design

We need a label design for a new company selling soy candles - Velvet Hearth Co.

We are using apothecary jars in 3 sizes.
As per attached candles will be dressed with a beautiful black bow and all finished with a diamante in centre of bow.

We would like label done on lid of candle jars - 5cm circle (5cm from one side to the other), this way one label will fit each product size. Label will be done as a sticker.

We are thinking of the background colour to be black, however are open to recommendations. We want label to be classy, elegant and simple.

Inspiration for candle design came from attached invitation that features the bow, and beautiful vintage paper on top area.

Label should include the following 3 pieces of information:
Velvet Hearth Co (company name)
Coconut Lime (this will change depending on fragrance)
Soy Candle

Velvet Hearth Co does not have a company logo... what is done for the label will set tone for what is done across other elements of business moving forward.

Industry/Entity Type

Business

Requirements
Must have
• Velvet Hearth Co
Fragrance Flavour
Soy Candle

```html
<!DOCTYPE html>
<html lang="en">
<head>
<meta charset="utf-8">
<title>Velvet Hearth Co — Coconut Lime Soy Candle Label</title>
<link href="https://fonts.googleapis.com/css2?family=Italianno&family=Tangerine:wght@700&family=Tinos&display=swap" rel="stylesheet">
<style>
  :root {
    --page: #ffffff;
    --label-black: #000000;
    --cream: #f4e4c9;
    --white: #ffffff;
    --ornament-soft: #d9d9d9;
  }
  html, body {
    margin: 0;
    padding: 0;
    width: 1200px;
    height: 1200px;
    overflow: hidden;
    background: var(--page);
  }
  .label {
    display: block;
    width: 1200px;
    height: 1200px;
  }
  .label-disc { fill: var(--label-black); }
  .brand-name {
    font-family: "Italianno", cursive;
    font-size: 160px;
    fill: var(--cream);
  }
  .fragrance-name {
    font-family: "Tinos", "Times New Roman", serif;
    font-size: 62px;
    fill: var(--white);
  }
  .product-type {
    font-family: "Tangerine", cursive;
    font-weight: 700;
    font-size: 140px;
    fill: var(--cream);
  }
</style>
</head>
<body>
<svg class="label" viewBox="0 0 1200 1200" xmlns="http://www.w3.org/2000/svg">
  <defs>
    <radialGradient id="flourish-tone" cx="50%" cy="50%" r="50%">
      <stop offset="0%" stop-color="var(--white)" stop-opacity="0.85"/>
      <stop offset="70%" stop-color="var(--ornament-soft)" stop-opacity="0.35"/>
      <stop offset="100%" stop-color="var(--ornament-soft)" stop-opacity="0"/>
    </radialGradient>
  </defs>

  <circle class="label-disc" cx="590" cy="528" r="518"/>

  <ellipse class="flourish flourish-top" cx="546" cy="148" rx="270" ry="80"
           fill="url(#flourish-tone)" role="img"
           aria-label="White scrolling vintage flourish ornament crowning the label"/>

  <text class="brand-name" x="523" y="432" text-anchor="middle"
        textLength="860" lengthAdjust="spacingAndGlyphs"
        transform="rotate(-4 523 400)">Velvet Hearth Co</text>

  <text class="fragrance-name" x="552" y="533" text-anchor="middle"
        textLength="456" lengthAdjust="spacingAndGlyphs">Coconut Lime</text>

  <ellipse class="flourish flourish-divider" cx="516" cy="658" rx="343" ry="64"
           fill="url(#flourish-tone)" role="img"
           aria-label="White symmetrical scroll flourish divider beneath the fragrance name"/>

  <text class="product-type" x="507" y="888" text-anchor="middle"
        textLength="449" lengthAdjust="spacingAndGlyphs">Soy Candle</text>
</svg>
</body>
</html>
```